Gardener needs an exciting new flyer design.

I'm a passionate gardener that requires a custom flyer design for a owner operator gardening business. Design will be for a DL flyer. I'm based on the Sunshine coast in Queensland Australia. My target audience is the residential market on the Sunshine coast. Business name is Tollmere Yards. My services are, lawn mowing, weeding, Eco Friendly fertilizing, green waste removal, Mulching, tree and shrub pruning, Full garden makeovers, hedging, pressure cleaning, privacy screening, Timber deck rejuvenation, Planting, Turf preparation and installation, and much more. Free no obligation quotes, reliable and friendly service, great rates. 12 years experience. Web www.tollmereyards.com.au - Phone 0418527036 - Email kip@tollmereyards.com.au I would like the design to portray a friendly and professional approach.

Target Market(s)

Residential

Industry/Entity Type

Gardener

Font styles to use
Serif

Colors
9ccb3b
abd037
3176b5

Requirements
Must have
• my services, my logo, my contact details,

```html
<!DOCTYPE html>
<html lang="en">
<head>
<meta charset="utf-8">
<title>Tollmere Yards – DL Flyer</title>
<link href="https://fonts.googleapis.com/css2?family=Fondamento&family=Open+Sans:wght@400;700&family=Oswald:wght@600&display=swap" rel="stylesheet">
<style>
  :root{
    --canvas:#d3d3d3;
    --label:#555555;
    --white:#ffffff;
    --forest:#2a5230;
    --panel:#2f7a3a;
    --leaf:#3b8236;
    --lime:#8fc641;
    --lime-soft:#9ccb3b;
    --badge-blue:#3176b5;
    --badge-purple:#5b2d6e;
    --badge-ribbon:#2aa2df;
  }
  *{margin:0;padding:0;box-sizing:border-box}
  html,body{width:1200px;height:1000px;overflow:hidden;background:var(--canvas)}
  body{position:relative;font-family:"Open Sans",Arial,sans-serif}
  .side-label{position:absolute;top:51px;font-size:11px;color:var(--label);letter-spacing:.3px;text-align:center;width:100px}
  .side-label--front{left:334px}
  .side-label--back{left:820px}
  .flyer{position:absolute;top:117px;height:791px;overflow:hidden}
  .flyer--front{left:173px;width:388px}
  .flyer--back{left:677px;width:389px}
  .flyer svg.backdrop{position:absolute;left:0;top:0}
  .brand-mark{position:absolute;left:50%;top:34px;width:86px;height:86px;margin-left:-43px;border-radius:50%}
  .flyer--front .brand-mark{background:var(--leaf)}
  .flyer--back .brand-mark{background:var(--white)}
  .brand-name{position:absolute;left:0;right:0;top:150px;text-align:center;font-family:"Fondamento",Georgia,serif;font-size:34px;line-height:1}
  .flyer--front .brand-name{color:var(--leaf)}
  .flyer--back .brand-name{color:var(--white)}
  .intro{position:absolute;left:40px;top:424px;width:172px;color:var(--white);font-size:12.4px;line-height:15.4px}
  .intro p{margin-bottom:15px}
  .contact{position:absolute;left:0;right:0;top:706px;text-align:center;color:var(--white)}
  .contact__phone{font-weight:700;font-size:23px;line-height:1;display:flex;justify-content:center;align-items:center;gap:2px}
  .contact__web{font-size:17px;line-height:1;margin-top:5px;display:flex;justify-content:center;align-items:center;gap:3px}
  .services{position:absolute;left:0;right:0;top:294px;text-align:center}
  .services h2{font-size:23px;font-weight:700;color:var(--leaf);line-height:1;margin-bottom:5px}
  .services ul{list-style:none;color:var(--white);font-size:14px;line-height:18.7px}
  .tagline{position:absolute;left:0;right:0;top:662px;text-align:center;font-family:"Oswald",Arial,sans-serif;font-weight:600;font-size:14.5px;line-height:18px;color:var(--white);text-transform:uppercase}
  .badge-text{font-family:"Open Sans",Arial,sans-serif;font-weight:700;fill:var(--white)}
</style>
</head>
<body>
  <div class="side-label side-label--front">FRONT</div>
  <div class="side-label side-label--back">BACK</div>

  <section class="flyer flyer--front">
    <svg class="backdrop" width="388" height="791" viewBox="0 0 388 791">
      <defs>
        <linearGradient id="gardenScene" x1="0" y1="0" x2="0" y2="1">
          <stop offset="0" stop-color="#8fae7c"/>
          <stop offset="1" stop-color="#4c8a34"/>
        </linearGradient>
        <linearGradient id="pathScene" x1="0" y1="0" x2="0" y2="1">
          <stop offset="0" stop-color="#4d7a42"/>
          <stop offset="1" stop-color="#9a8fbf"/>
        </linearGradient>
      </defs>
      <rect width="388" height="791" fill="var(--white)"/>
      <rect y="193" width="388" height="225" fill="url(#gardenScene)" role="img" aria-label="Photo of a landscaped garden with lawn, flower beds and trees"/>
      <polygon points="0,418 388,366 388,400 0,430" fill="var(--lime)"/>
      <rect x="224" y="395" width="164" height="285" fill="url(#pathScene)" role="img" aria-label="Photo of a stepping-stone garden path lined with lavender"/>
      <polygon points="0,412 224,404 224,675 0,690" fill="var(--panel)"/>
      <polygon points="0,690 388,665 388,791 0,791" fill="var(--forest)"/>
      <g class="experience-badge" transform="translate(312,656)">
        <circle r="38" fill="var(--badge-purple)"/>
        <circle r="29" fill="var(--white)"/>
        <circle r="25" fill="var(--badge-blue)"/>
        <polygon points="-50,12 50,12 45,23 50,34 -50,34 -45,23" fill="var(--badge-ribbon)"/>
        <text class="badge-text" y="2" text-anchor="middle" font-size="22">12</text>
        <text class="badge-text" y="14" text-anchor="middle" font-size="10">YEARS</text>
        <text class="badge-text" y="28" text-anchor="middle" font-size="11">EXPERIENCE</text>
      </g>
    </svg>

    <div class="brand-mark"></div>
    <div class="brand-name">Tollmere Yards</div>

    <div class="intro">
      <p>Tollmere Yards is your garden and lawn care specialist, with a passion for gardening and a keen eye for detail you can rest assured you're in the right hands.</p>
      <p>My services are tailored to meet every individual clients needs.</p>
      <p>From a one time mow too regular lawn mowing, all aspects of garden care and even full garden makeovers.</p>
    </div>

    <div class="contact">
      <div class="contact__phone">
        <svg width="16" height="18" viewBox="0 0 16 18"><path d="M3 1l3 0 1.5 4-2 1.5c1 2.5 2.5 4 5 5L12 9.5l4 1.5v3c0 1.5-1.5 3-3 2.5C7 15 2 10 1 4 .8 2.5 1.5 1 3 1z" fill="var(--lime)"/></svg>
        0418527036
      </div>
      <div class="contact__web">
        <svg width="16" height="16" viewBox="0 0 16 16"><circle cx="8" cy="8" r="7" fill="none" stroke="var(--lime)" stroke-width="1.6"/><path d="M1 8h14M8 1c3 3.5 3 10.5 0 14M8 1c-3 3.5-3 10.5 0 14" fill="none" stroke="var(--lime)" stroke-width="1.3"/></svg>
        www.tollmereyards.com.au
      </div>
    </div>
  </section>

  <section class="flyer flyer--back">
    <svg class="backdrop" width="389" height="791" viewBox="0 0 389 791">
      <defs>
        <linearGradient id="grassScene" x1="0" y1="0" x2="0" y2="1">
          <stop offset="0" stop-color="#8fc641" stop-opacity="0"/>
          <stop offset=".45" stop-color="#7fbd3a"/>
          <stop offset="1" stop-color="#3f7d22"/>
        </linearGradient>
      </defs>
      <rect width="389" height="791" fill="var(--forest)"/>
      <polygon points="0,232 389,258 389,791 0,791" fill="var(--lime)"/>
      <rect y="500" width="389" height="170" fill="url(#grassScene)" role="img" aria-label="Close-up photo of fresh green lawn grass"/>
      <polygon points="0,633 389,660 389,791 0,791" fill="var(--forest)"/>
    </svg>

    <div class="brand-mark"></div>
    <div class="brand-name">Tollmere Yards</div>

    <div class="services">
      <h2>SERVICES</h2>
      <ul>
        <li>Lawn mowing,</li>
        <li>Weeding,</li>
        <li>Eco Friendly fertilizing,</li>
        <li>Green waste removal,</li>
        <li>Mulching,</li>
        <li>Tree and shrub pruning,</li>
        <li>Full garden makeovers,</li>
        <li>Hedging,</li>
        <li>Pressure cleaning,</li>
        <li>Privacy screening,</li>
        <li>Timber deck rejuvenation,</li>
        <li>Planting,</li>
        <li>Turf preparation and installation,</li>
        <li>and much more.</li>
      </ul>
    </div>

    <div class="tagline">Transform your garden today<br>into a masterpiece you'll be proud of.</div>

    <div class="contact">
      <div class="contact__phone">
        <svg width="16" height="18" viewBox="0 0 16 18"><path d="M3 1l3 0 1.5 4-2 1.5c1 2.5 2.5 4 5 5L12 9.5l4 1.5v3c0 1.5-1.5 3-3 2.5C7 15 2 10 1 4 .8 2.5 1.5 1 3 1z" fill="var(--lime)"/></svg>
        0418527036
      </div>
      <div class="contact__web">
        <svg width="16" height="16" viewBox="0 0 16 16"><circle cx="8" cy="8" r="7" fill="none" stroke="var(--lime)" stroke-width="1.6"/><path d="M1 8h14M8 1c3 3.5 3 10.5 0 14M8 1c-3 3.5-3 10.5 0 14" fill="none" stroke="var(--lime)" stroke-width="1.3"/></svg>
        www.tollmereyards.com.au
      </div>
    </div>
  </section>
</body>
</html>
```